New Business Card Design Project

We need to enhance the look and feel of our brand. We are starting with the business card and will hopefully expand to letter head, website, etc. The firm is based in Kolding Denmark and invests with global pension funds and for mutual fund investors alike. We would like to see an innovative use of the companies logo (star on the website - www.tidemarkharbor.com) and a broader use of a color palette. Presently it is dominantly shades of blue. The firm wants to convey a sense they are a creative investment team that understands all the risks in the emerging markets and have the skills to perform in an environment of uncertainty.

Presently, we have three locations: Kolding Denmark, Glendale CA USA, Zurich Switzerland. We also have a prominently displayed bar code square on a solid dark blue back that will take smart phone users to the firm's website. I am indifferent to its inclusion., Details for my new Business Card Design Project will be added soon.
Updates

Reason: Designers, I am working with on getting feedback from both US and Danish partners on preferences. That is taking slightly more time than expected. Thanks for you patience. Nice work. PLM

Target Market(s)

The target market is a combination of institutional and retail investors. The european arm uses a card similar to a couple of those submitted.

Industry/Entity Type

Environment

Requirements
Must have
• The company's Star Logo. See www.tidemarkharbor.com. It may be used in its current form or some new clever way. The founders are Danish and have a strong affinity for it.
Nice to have
• The new materials may be solely used in the north America and distributed in Australia as well. Therefore, we may try something new in these markets. I'd prefer to see a broader use of the color spectrum, not simply blue.
Should not have
• The card should not look and feel like a bank, insurance company, or a traditional money manager.

```html
<!DOCTYPE html>
<html lang="en">
<head>
<meta charset="utf-8">
<title>TidemarkHarbor Business Cards</title>
<link rel="stylesheet" href="https://fonts.googleapis.com/css2?family=Open+Sans:wght@400;700&display=swap">
<style>
  :root {
    --navy: #0f4170;
    --cyan: #3bbde6;
    --sky: #bfe6f7;
    --ink: #000000;
    --paper: #ffffff;
    --silver: #b9bcc0;
    --stage: #e8e9eb;
    --label-grey: #6b6b6b;
  }
  * { box-sizing: border-box; margin: 0; padding: 0; }
  html, body { width: 1200px; height: 927px; overflow: hidden; }
  body {
    background: var(--stage);
    font-family: "Open Sans", Arial, sans-serif;
    position: relative;
  }
  .card {
    position: absolute;
    width: 520px;
    height: 300px;
    overflow: hidden;
    box-shadow: 0 6px 18px rgba(0,0,0,0.18);
  }
  .card--dark { background: var(--ink); }
  .card--light { background: var(--paper); }
  .card svg.card__art { position: absolute; inset: 0; }

  .pos-a { left: 60px;  top: 100px; }
  .pos-b { left: 620px; top: 100px; }
  .pos-c { left: 60px;  top: 527px; }
  .pos-d { left: 620px; top: 527px; }

  /* Front face */
  .front__brand {
    position: absolute;
    top: 40px; left: 0; right: 0;
    display: flex; flex-direction: column; align-items: center; gap: 10px;
  }
  .brand-dot {
    width: 74px; height: 74px; border-radius: 50%;
  }
  .card--dark .brand-dot { border: 8px solid var(--paper); }
  .card--light .brand-dot { background: var(--cyan); }
  .brand-name {
    font-weight: 700;
    font-size: 34px;
    letter-spacing: -0.5px;
  }
  .card--dark .brand-name { color: var(--paper); }
  .card--light .brand-name { color: var(--navy); }
  .front__url {
    position: absolute;
    bottom: 18px; left: 0; right: 0;
    text-align: center;
    font-weight: 700;
    font-size: 22px;
    color: var(--ink);
  }

  /* Back face */
  .back__details {
    position: absolute;
    left: 230px; right: 14px; top: 22px;
    text-align: center;
  }
  .back__brand {
    font-weight: 700; font-size: 30px; letter-spacing: -0.5px;
    text-align: right; margin-bottom: 26px;
  }
  .back__name { font-weight: 700; font-size: 18px; }
  .back__role { font-size: 15px; margin-bottom: 28px; }
  .back__contact { font-weight: 700; font-size: 15px; line-height: 1.55; }

  .card--dark .back__brand,
  .card--dark .back__name,
  .card--dark .back__contact { color: var(--paper); }
  .card--dark .back__role { color: #d6d6d6; }
  .card--light .back__brand { color: var(--cyan); }
  .card--light .back__name,
  .card--light .back__role,
  .card--light .back__contact { color: var(--navy); }
</style>
</head>
<body>

<svg width="0" height="0" style="position:absolute" aria-hidden="true">
  <defs>
    <linearGradient id="disc-fill" x1="1" y1="0" x2="0" y2="1">
      <stop offset="0" stop-color="#0f4170"/>
      <stop offset="0.55" stop-color="#2a78b4"/>
      <stop offset="1" stop-color="#bfe6f7"/>
    </linearGradient>
    <linearGradient id="silver-fill" x1="0" y1="0" x2="1" y2="0">
      <stop offset="0" stop-color="#ffffff"/>
      <stop offset="0.5" stop-color="#9ea2a7"/>
      <stop offset="1" stop-color="#e6e7e9"/>
    </linearGradient>
  </defs>
</svg>

<!-- Dark back: contact side -->
<section class="card card--dark pos-a">
  <svg class="card__art" viewBox="0 0 520 300">
    <circle cx="-40" cy="170" r="265" fill="#3bbde6"/>
    <circle cx="-40" cy="170" r="232" fill="url(#disc-fill)" role="img" aria-label="Decorative disc in shades of blue"/>
  </svg>
  <div class="back__details">
    <div class="back__brand">TidemarkHarbor</div>
    <div class="back__name">Anders Holmvik</div>
    <div class="back__role">President</div>
    <div class="back__contact">anders@tidemarkharbor.com<br>45 210 3390</div>
  </div>
</section>

<!-- Dark front: brand side -->
<section class="card card--dark pos-b">
  <svg class="card__art" viewBox="0 0 520 300" preserveAspectRatio="none">
    <path d="M0 218 C 180 214 360 200 520 168 L520 182 C 360 210 180 226 0 232 Z" fill="url(#silver-fill)"/>
    <path d="M0 232 C 180 226 360 210 520 182 L520 196 C 360 222 180 238 0 244 Z" fill="var(--navy)"/>
    <path d="M0 244 C 180 238 360 222 520 184 L520 300 L0 300 Z" fill="var(--cyan)"/>
  </svg>
  <div class="front__brand">
    <span class="brand-dot"></span>
    <span class="brand-name">TidemarkHarbor</span>
  </div>
  <div class="front__url">www.tidemarkharbor.com</div>
</section>

<!-- Light front: brand side -->
<section class="card card--light pos-c">
  <svg class="card__art" viewBox="0 0 520 300" preserveAspectRatio="none">
    <path d="M0 218 C 180 214 360 200 520 168 L520 182 C 360 210 180 226 0 232 Z" fill="url(#silver-fill)"/>
    <path d="M0 232 C 180 226 360 210 520 182 L520 196 C 360 222 180 238 0 244 Z" fill="var(--navy)"/>
    <path d="M0 244 C 180 238 360 222 520 184 L520 300 L0 300 Z" fill="var(--cyan)"/>
  </svg>
  <div class="front__brand">
    <span class="brand-dot"></span>
    <span class="brand-name">TidemarkHarbor</span>
  </div>
  <div class="front__url">www.tidemarkharbor.com</div>
</section>

<!-- Light back: contact side -->
<section class="card card--light pos-d">
  <svg class="card__art" viewBox="0 0 520 300">
    <circle cx="-40" cy="170" r="265" fill="#3bbde6"/>
    <circle cx="-40" cy="170" r="232" fill="url(#disc-fill)" role="img" aria-label="Decorative disc in shades of blue"/>
  </svg>
  <div class="back__details">
    <div class="back__brand">TidemarkHarbor</div>
    <div class="back__name">Anders Holmvik</div>
    <div class="back__role">President</div>
    <div class="back__contact">anders@tidemarkharbor.com<br>45 210 3390</div>
  </div>
</section>

</body>
</html>
```